Website Header Development

I am after a redesign of the Header of a website www.kaltroweb.com.au.
This project is for the header only, and should fit in with the rest of the site
Target Market(s)
Business
Requirements
Should not have
- Over the top. Keep it simple

```html
<!DOCTYPE html>
<html lang="en">
<head>
<meta charset="utf-8">
<title>Kaltro Energy – Resource Efficiency</title>
<link rel="stylesheet" href="https://fonts.googleapis.com/css2?family=Alegreya:wght@700&family=Alegreya+Sans:wght@400;700&family=Lato:wght@400;700&display=swap">
<style>
  :root {
    --backdrop: #f4f4f4;
    --page: #ffffff;
    --banner-deep: #0b2468;
    --banner-mid: #1f58a8;
    --banner-light: #4a9ae0;
    --nav-green: #2f8a3d;
    --nav-green-dark: #256f31;
    --nav-green-light: #3a9a48;
    --nav-text: #ffffff;
    --brand: #16285e;
    --brand-mark: #2a56b8;
    --heading: #14146a;
    --side-heading: #1f3a7a;
    --body-text: #2a2a2a;
    --field-border: #cfcfcf;
    --photo-light: #e6eaee;
    --photo-mid: #c8ccd2;
    --photo-skin: #d7b29e;
  }
  * { box-sizing: border-box; margin: 0; padding: 0; }
  html, body {
    width: 1200px; height: 678px; overflow: hidden;
    background: var(--backdrop);
  }
  .page {
    position: absolute; left: 40px; top: 0;
    width: 1000px; height: 605px;
    background: var(--page);
    transform: scale(1.12); transform-origin: 0 0;
    overflow: hidden;
    font-family: "Alegreya Sans", sans-serif;
    color: var(--body-text);
  }
  .banner {
    position: absolute; left: 0; top: 0; width: 1000px; height: 115px;
    background: linear-gradient(100deg, var(--banner-deep) 0%, var(--banner-deep) 30%, var(--banner-mid) 60%, var(--banner-light) 100%);
  }
  .brand {
    position: absolute; left: 40px; top: 48px;
    display: flex; align-items: center; gap: 12px;
  }
  .brand-name {
    font-family: "Alegreya Sans", sans-serif; font-weight: 700;
    font-size: 36px; line-height: 1; color: #ffffff; letter-spacing: -0.5px;
  }
  .brand-mark { width: 30px; height: 30px; background: var(--brand-mark); }
  .main-nav {
    position: absolute; left: 0; top: 115px; width: 1000px; height: 50px;
    background: var(--nav-green);
  }
  .main-nav svg { position: absolute; right: 0; top: 0; }
  .nav-item {
    position: absolute; top: 0; height: 50px; display: flex; align-items: center;
    font-family: "Lato", sans-serif; font-size: 11px; color: var(--nav-text);
  }
  .nav-item.primary { font-weight: 700; font-size: 13.5px; padding-top: 8px; }
  .nav-item.secondary { padding-bottom: 7px; }
  .content-title {
    position: absolute; left: 60px; top: 195px; width: 586px; text-align: center;
    font-family: "Alegreya", serif; font-weight: 700; font-size: 23px; color: var(--heading);
  }
  .intro {
    position: absolute; left: 60px; top: 245px; width: 580px;
    font-size: 14.5px; line-height: 25px;
  }
  .intro p { margin-bottom: 26px; width: 200px; }
  .intro p.wide { width: 580px; }
  .feature-photo {
    position: absolute; left: 288px; top: 257px; width: 350px; height: 233px;
    background: linear-gradient(90deg, var(--photo-light) 0%, var(--photo-skin) 22%, var(--photo-light) 45%, var(--photo-mid) 75%, var(--photo-light) 100%);
  }
  .sidebar { position: absolute; left: 736px; top: 166px; width: 190px; }
  .search-field {
    width: 184px; height: 31px; border: 1px solid var(--field-border);
    display: flex; align-items: center; gap: 7px; padding-left: 8px;
    font-family: Arial, sans-serif; font-size: 14px; color: #9a9a9a;
  }
  .newsletter-title {
    margin-top: 38px;
    font-family: "Alegreya", serif; font-weight: 700; font-size: 21px;
    line-height: 30px; letter-spacing: 2px; color: var(--side-heading);
  }
  .newsletter-note {
    margin-top: 24px; font-weight: 700; font-size: 10.5px; line-height: 25px; color: #1a1a1a;
  }
  .text-field { width: 183px; height: 34px; border: 1px solid var(--field-border); margin: 8px 0 14px; }
</style>
</head>
<body>
<div class="page">
  <header class="banner">
    <div class="brand">
      <span class="brand-name">kaltro energy</span>
      <span class="brand-mark"></span>
    </div>
  </header>
  <nav class="main-nav">
    <svg width="100" height="50" viewBox="0 0 100 50" aria-hidden="true">
      <polygon points="0,0 100,0 100,50 50,50" fill="var(--nav-green-dark)"/>
    </svg>
    <span class="nav-item primary" style="left:84px">Home</span>
    <span class="nav-item secondary" style="left:159px">About Us</span>
    <span class="nav-item secondary" style="left:238px">Services</span>
    <span class="nav-item secondary" style="left:311px">Projects and Case Studies</span>
    <span class="nav-item primary" style="left:474px">Financial Information</span>
    <span class="nav-item secondary" style="left:651px">News</span>
    <span class="nav-item secondary" style="left:711px">Contact</span>
  </nav>

  <h1 class="content-title">Resource Efficiency – Sustainable Solutions</h1>
  <div class="intro">
    <p>Is your business performing as well as your competitors?</p>
    <p>Are your fixed costs comparable to industry leaders?</p>
    <p>Is your business becoming less profitable with increased energy, waste and water prices?</p>
    <p class="wide"><span style="display:block;width:200px">Do you wish to reduce your</span>impact on the environment through reducing the use of resources (energy, waste and water) within your business?</p>
  </div>
  <div class="feature-photo" role="img" aria-label="Photo of a businessman holding up a jigsaw piece beside a puzzle labelled Solution"></div>

  <aside class="sidebar">
    <div class="search-field">
      <svg width="14" height="14" viewBox="0 0 14 14" aria-hidden="true">
        <circle cx="5.5" cy="5.5" r="4.2" fill="none" stroke="#9a9a9a" stroke-width="2"/>
        <line x1="8.6" y1="8.6" x2="13" y2="13" stroke="#9a9a9a" stroke-width="2.2"/>
      </svg>
      Search
    </div>
    <h2 class="newsletter-title">Kaltro<br>Energy<br>Newsletter</h2>
    <p class="newsletter-note">Would you like to receive our regular monthly Newsletter? Please fill in your Name:</p>
    <div class="text-field"></div>
    <p class="newsletter-note" style="margin-top:0">Let us know your email address so we can send the Newsletter directly to your email address. (Note that your details will not be passed onto any 3rd parties. Your details stricly remain with</p>
  </aside>
</div>
</body>
</html>
```